Plastic Surgeon Stationery Design for a female surgeon

I would like a modern-classic stationery design ... I'm a 46 y.o plastic surgeon from Brasil and recently changed my life ( I was a navy surgeon for 18 years) . Now I'm on my office in Rio de Janeiro and I would like a classy design .
I have a fanpage with 76.000 followers on facebook and 12000 on instagram, and I love social media.
I like the colours like brown, beige ( something that I can use with the picture I'm attaching).

Target Market(s)

people who loves beauty, life

Industry/Entity Type

Plastic

Contact Information for Business Card

Dra Helena Moura de Castanheda e Lobo
Cirurgiã Plástica - Estética e Reconstrutiva
CRM 47.38592- 3 RQE 5813

Av. dos Coqueirais 3847 bl 03 cob 05
Vila do Sabiá - RJ - CEP 24587-000

Cons : (21) 2738-5169 Celular: (21) 97452-3361
helenamoura@caixapostal-exemplo.com

Logo Text

Helena de Castanheda - Cirurgiã Plástica

Font styles to use
Other font styles liked:
• I like the Scrip fonts but I'm open to sugestions

Colors
fbe7d2
ffffff
f8ba93
fee3d4
f9ba93
919191
757575
5c5c5c
9d9d9d

Requirements
Must have
• I would like my logo with something related to my initials and easy to use on merchandising stuff like pens, bags ...
Nice to have
• things related to happiness , graffic contents ( I love forms)
Should not have
• the plastic surgery cliches like female bodies , breasts , human parts ...

```html
<!DOCTYPE html>
<html lang="pt-BR">
<head>
<meta charset="utf-8">
<title>Helena de Castanheda – Cartão de visita</title>
<link rel="stylesheet" href="https://fonts.googleapis.com/css2?family=Source+Sans+3:wght@400&display=swap">
<style>
  :root {
    --page-bg: #e9e4df;
    --card-white: #ffffff;
    --peach-light: #fee3d4;
    --peach-soft: #fbe7d2;
    --peach: #f8ba93;
    --peach-deep: #e9a98c;
    --grey-dark: #5c5c5c;
    --grey-mid: #757575;
    --grey-line: #9d9d9d;
  }
  * { box-sizing: border-box; margin: 0; padding: 0; }
  html, body {
    width: 1200px; height: 1200px; overflow: hidden;
    background: var(--page-bg);
    font-family: "Source Sans 3", "Myriad Pro", Arial, sans-serif;
  }
  .business-card {
    position: absolute; left: 80px; top: 265px;
    width: 1040px; height: 670px; overflow: hidden;
    background:
      radial-gradient(ellipse 70% 55% at 75% 105%, #f3b89a 0%, #f9d3b7 35%, rgba(255,240,225,0.6) 65%, rgba(255,255,255,0) 85%),
      linear-gradient(180deg, var(--card-white) 0%, var(--card-white) 55%, var(--peach-soft) 100%);
    box-shadow: 0 10px 30px rgba(0,0,0,0.18);
  }
  .portrait {
    position: absolute; left: 0; top: 0; width: 480px; height: 670px;
  }
  .brand {
    position: absolute; left: 514px; top: 200px;
    display: flex; align-items: center;
  }
  .brand-dot {
    width: 100px; height: 100px; border-radius: 50%;
    background: var(--peach);
  }
  .brand-divider {
    width: 2px; height: 150px; margin: 0 20px 0 30px;
    background: var(--grey-line);
  }
  .brand-name {
    color: var(--peach);
    font-size: 52px; font-weight: 400; line-height: 54px;
    letter-spacing: 0.5px; text-transform: uppercase;
  }
  .credentials {
    position: absolute; left: 480px; width: 534px; top: 412px;
    text-align: center; color: var(--grey-dark);
    font-size: 23px; line-height: 31px;
  }
</style>
</head>
<body>
  <div class="business-card">
    <svg class="portrait" viewBox="0 0 480 670" role="img" aria-label="Retrato da cirurgiã sorrindo, cabelos castanhos, blusa branca e colar de pérolas">
      <defs>
        <radialGradient id="portraitTone" cx="0.5" cy="0.55" r="0.6">
          <stop offset="0" stop-color="#d9a98e"/>
          <stop offset="0.45" stop-color="#7a5545"/>
          <stop offset="0.75" stop-color="#c9b8ae" stop-opacity="0.6"/>
          <stop offset="1" stop-color="#ffffff" stop-opacity="0"/>
        </radialGradient>
      </defs>
      <rect width="480" height="670" fill="url(#portraitTone)"/>
    </svg>

    <div class="brand">
      <div class="brand-dot"></div>
      <div class="brand-divider"></div>
      <div class="brand-name">Helena<br>de<br>Castanheda</div>
    </div>

    <p class="credentials">
      Cirurgiã Plástica - Estética e Reconstrutiva<br>
      CRM 47.38592- 3 RQE 5813
    </p>
  </div>
</body>
</html>
```